Geschäftspapiere für mobile Cocktailbar
Zielgruppe
Wir sind eine mobile Cocktailbar ! Wir arbeiten vielen Veranstaltungen / Festivals.
Ein sehr wichtiges Geschäftssegment sind Firmenveranstaltungen jeglicher Größe.
Hier stehen wir für sehr hohe Qualität an Service und an den Drinks.
Wir arbeiten stets mit Markenprodukten, professionellen Barkeepern und sehr hochwertigen Equipment
Unsere Website ist www.korbinel-bar.de
Aufgabenstellung
Es soll schlicht aber hochwertig sein
vielleicht eine Layout im Hintergrund
Drinks, Flüssigkeit, Bartending etc
Gerne auch das Logo eingebaut

```html
<!DOCTYPE html>
<html lang="de">
<head>
<meta charset="utf-8">
<title>Korbinel Bar – Briefbogen</title>
<link href="https://fonts.googleapis.com/css2?family=Roboto+Condensed:wght@300;400&display=swap" rel="stylesheet">
<style>
  :root {
    --paper: #ffffff;
    --ink: #000000;
    --ink-inverse: #ffffff;
    --muted: #7a7a7a;
    --watermark: #f1f1f1;
  }
  * { margin: 0; padding: 0; box-sizing: border-box; }
  html, body { width: 849px; height: 1200px; overflow: hidden; background: var(--paper); }
  .letterhead {
    position: relative;
    width: 849px;
    height: 1200px;
    background: var(--paper);
    font-family: "Roboto Condensed", sans-serif;
    font-weight: 300;
  }
  .sender-line {
    position: absolute;
    left: 80px;
    top: 186px;
    font-size: 14.5px;
    color: var(--muted);
  }
  .contact-panel {
    position: absolute;
    left: 510px;
    top: 0;
    width: 255px;
    height: 353px;
    background: var(--ink);
    border-radius: 0 0 34px 34px;
    color: var(--ink-inverse);
  }
  .brand-name {
    position: absolute;
    left: 17px;
    top: 46px;
    width: 224px;
    text-align: center;
    font-family: "Roboto Condensed", sans-serif;
    font-weight: 400;
    font-size: 21px;
    line-height: 26px;
    color: var(--ink-inverse);
  }
  .contact-name {
    position: absolute;
    left: 68px;
    top: 112px;
    font-size: 19px;
  }
  .contact-row {
    position: absolute;
    left: 29px;
    display: flex;
    align-items: center;
    gap: 12px;
    font-size: 19px;
    line-height: 20px;
  }
  .contact-row .icon {
    width: 26px;
    height: 26px;
    flex: none;
    border-radius: 50%;
    background: var(--ink-inverse);
    display: flex;
    align-items: center;
    justify-content: center;
  }
  .row-address { top: 155px; }
  .row-phone { top: 211px; }
  .row-mail { top: 249px; }
  .row-web { top: 289px; }
  .bar-motif {
    position: absolute;
    left: 258px;
    top: 612px;
    width: 311px;
    height: 320px;
    border-radius: 40%;
    background: radial-gradient(ellipse at center, var(--watermark) 0%, rgba(241,241,241,0.5) 55%, rgba(255,255,255,0) 75%);
  }
</style>
</head>
<body>
<main class="letterhead">
  <p class="sender-line">Korbinel Bar, Lindenhofstraße. 42, 80469 München</p>

  <aside class="contact-panel">
    <div class="brand-name">Korbinel Bar</div>

    <p class="contact-name">Marito Blauf</p>

    <div class="contact-row row-address">
      <span class="icon">
        <svg width="14" height="16" viewBox="0 0 14 16" fill="none" stroke="#000" stroke-width="1.3">
          <path d="M7 15s5-5 5-9A5 5 0 0 0 2 6c0 4 5 9 5 9z"/>
          <circle cx="7" cy="6" r="2"/>
        </svg>
      </span>
      <span>Lindenhofstr. 42<br>80469 München</span>
    </div>

    <div class="contact-row row-phone">
      <span class="icon">
        <svg width="14" height="14" viewBox="0 0 24 24" fill="none" stroke="#000" stroke-width="2">
          <path d="M22 16.9v3a2 2 0 0 1-2.2 2 19.8 19.8 0 0 1-8.6-3.1 19.5 19.5 0 0 1-6-6A19.8 19.8 0 0 1 2.1 4.2 2 2 0 0 1 4.1 2h3a2 2 0 0 1 2 1.7c.1 1 .4 1.9.7 2.8a2 2 0 0 1-.5 2.1L8 9.9a16 16 0 0 0 6 6l1.3-1.3a2 2 0 0 1 2.1-.4c.9.3 1.8.6 2.8.7a2 2 0 0 1 1.7 2z"/>
        </svg>
      </span>
      <span>+49 89 555 012 34</span>
    </div>

    <div class="contact-row row-mail">
      <span class="icon">
        <svg width="15" height="11" viewBox="0 0 15 11" fill="none" stroke="#000" stroke-width="1.2">
          <rect x="0.6" y="0.6" width="13.8" height="9.8" rx="1"/>
          <path d="M1 1l6.5 5L14 1"/>
        </svg>
      </span>
      <span>info@korbinel-bar.de</span>
    </div>

    <div class="contact-row row-web">
      <span class="icon">
        <svg width="16" height="16" viewBox="0 0 16 16" fill="none" stroke="#000" stroke-width="1.1">
          <circle cx="8" cy="8" r="7"/>
          <ellipse cx="8" cy="8" rx="3" ry="7"/>
          <path d="M1 8h14M2 4.5h12M2 11.5h12"/>
        </svg>
      </span>
      <span>www.korbinel-bar.de</span>
    </div>
  </aside>

  <div class="bar-motif" role="img" aria-label="Faint line illustration of a cocktail glass with a citrus slice and straw"></div>
</main>
</body>
</html>
```